Bref créative
Kestrel Medics Facility Brochure
Pain Management & Physical Therapy Center
Relieving Pain Restoring Mobility Renewing Hope
300 DPI, CMYK, 2 Panel Brochure - 7.9 inches width and 9 inches tall including 1/4 inch bleed. (The same folded size as a 3 panel brochure, but using just 2 panels for this brochure.) Usually stay with blues. Approximate CMYK of blue is 93, 64, 14, 1. Photos can't be in boxes if possible. Owners like "cutouts" of images.
Health
All possible patients.
1.) Finding relief... Whether your pain is caused by an injury, severe arthritis or a degenrative disease, we can help you find relief and regain your quality of life.
2.) TREATMENTS INCLUDE: (Don't include letters for each treatment.)
a.) Knee Pain/Hip Pain/Arthritis
With programs nationally acclaimed by the Joint Care Guild of Tovaria, KMB uses a combination of treatments for eliminating or reducing pain quickly. Many patients with osteoarthritis may get pain relief after just one treatment. Over the last decade, our programs have helped over 5,000 patients regain their quality of life without surgery. For more information or to view success stories, visit www.zeroachelimbs.example.
b.) Back Pain/Sciatica/Neck Pain
Our pain management treatment team, which includes a Lindqvist Institute trained physician, physical therapists, and chiropractic physicians, utilizes a multi-disciplinary approach to your pain care. If back pain is affecting your quality of life, let KMB provide you with an accurate diagnosis, rapid relief, and long lasting results.
c.) Tennis Elbow/Rotator Cuff/Sports Injuries
KMB’s Platelet Rich Plasma (PRP) Program is the most advanced, cutting edge therapy program in the bi-state area. Using PRP, Derek Vallano, MD, can relieve your pain quickly and in a most effective way by using your blood platelets. By enhancing the tissue recovery through this unique program, athletes can get back to competition quicker, workers can return to work faster, and the average person can return to his or her daily activities quickly. For more information about PRP, visit www.kmbrelief.example and get your questions answered.
d.) Peripheral Neuropathy Program (PNP)
KMB has a solution for the irritating numbness, burning, and pain in your legs and feet. Our practice uses innovative treatment programs that will relieve your symptoms using medical treatments that are safe, effective and most importantly, require no surgery.
e.) And more...
SI Joint Pain, Tennis Elbow, Migraines, Headaches
About Kestrel Medics Bureau (KMB):
KMB is a one-of-a-kind integrated medical facility that combines the expertise of a Board Certified, Lindqvist Institute trained, Pain
Management MD, and a team of physician assistants, nurse practitioners, chiropractic physicians, and physical therapists utilizing KinetraTM therapy.
The KMB Advantage:
All providers under one roof
Less driving - One co-pay - Save time
Outside PT referrals accepted
Most insurances accepted
Personal Injury/Work Comp accepted
Multiple Metro Locations
Tovaria: Ashdel, Brennick, Marlow, & Eastvale
Corvane: Lindhurst
To schedule an appointment with Kestrel Medics Bureau (KMB) call 888.555.0142 today! (or something to that effect)
web: kmbrelief.example
blog: kmbnotes.example
The logo is attached. The font for the logo is Trajan Pro Bold above KMB letters and regular below KMB letters

```html
<!DOCTYPE html>
<html lang="en">
<head>
<meta charset="utf-8">
<title>Kestrel Medics Facility Brochure</title>
<link href="https://fonts.googleapis.com/css2?family=Cinzel:wght@400;700&family=Lato:wght@400;700&display=swap" rel="stylesheet">
<style>
:root{
  --blue:#1b5da8;
  --blue-deep:#0f3f7d;
  --blue-light:#5b95d2;
  --sky:#cfe1f3;
  --ink:#2b2f36;
  --paper:#ffffff;
  --stage:#8a8d92;
}
*{box-sizing:border-box;margin:0;padding:0}
html,body{width:1200px;height:941px;overflow:hidden;background:var(--stage)}
.canvas{position:relative;width:1200px;height:941px}
.spread{position:absolute;top:163px;width:540px;height:615px;display:flex;box-shadow:0 4px 14px rgba(0,0,0,.3)}
.spread--outside{left:40px}
.spread--inside{left:620px}
.panel{position:relative;width:270px;height:615px;background:var(--paper);overflow:hidden;font-family:Lato,sans-serif;color:var(--ink)}
.panel + .panel{border-left:1px solid #e3e8ee}
.wave{position:absolute;left:0;width:270px}
.serif{font-family:Cinzel,serif}

/* outside left */
.about-block{position:absolute;left:0;top:0;width:270px;height:395px;background:linear-gradient(180deg,var(--blue) 0%,var(--blue-deep) 100%);padding:18px 18px;color:#fff}
.about-block h3{font-family:Cinzel,serif;font-weight:700;font-size:9.5px;letter-spacing:.3px;margin-bottom:6px}
.about-block p{font-size:7px;line-height:1.5;margin-bottom:12px}
.advantage{list-style:none;font-size:7px;line-height:1.65;margin-bottom:12px}
.advantage li::before{content:"";display:inline-block;width:4px;height:4px;background:#fff;border-radius:50%;margin-right:6px;vertical-align:middle}
.schedule{font-size:7px;font-style:italic;line-height:1.5;margin-bottom:6px}
.call{font-family:Cinzel,serif;font-weight:700;font-size:13px;line-height:1.3}
.contact-lower{position:absolute;left:18px;top:470px;width:234px;font-size:7.5px;line-height:1.6;color:var(--blue-deep)}
.contact-lower .serif{font-weight:700;font-size:9px}

/* cover */
.logo{position:absolute;top:22px;left:0;width:270px;display:flex;align-items:center;justify-content:center;gap:7px}
.logo-dot{width:12px;height:12px;border-radius:50%;background:var(--blue)}
.logo-name{font-family:Cinzel,serif;font-weight:700;font-size:12px;color:var(--blue-deep);letter-spacing:.4px}
.title-band{position:absolute;top:70px;right:0;width:175px;height:100px;background:linear-gradient(90deg,var(--blue-light),var(--blue));color:#fff;font-family:Cinzel,serif;font-size:12px;line-height:1.45;text-align:center;padding:20px 10px}
.cover-photo{position:absolute;top:170px;left:0;width:270px;height:290px;background:linear-gradient(180deg,var(--sky) 0%,#e6eef6 55%,#a9b98b 100%)}
.url{position:absolute;bottom:22px;width:100%;text-align:center;font-family:Cinzel,serif;font-weight:700;font-size:9px;color:var(--blue-deep)}

/* inside */
.band{height:18px;background:linear-gradient(90deg,var(--blue),var(--blue-light));color:#fff;font-family:Cinzel,serif;font-weight:700;font-size:10px;line-height:18px;padding-left:14px;margin:0 0 6px}
.copy{padding:0 14px;font-size:6.4px;line-height:1.5}
.copy h4{font-family:Cinzel,serif;font-weight:700;font-size:7.6px;color:var(--blue);margin:6px 0 2px}
.copy p{margin-bottom:4px}
.inside-left .band:first-child{margin-top:16px}
.back-photo{position:absolute;left:20px;top:340px;width:150px;height:190px;border-radius:45% 45% 10% 10%;background:radial-gradient(ellipse at 50% 40%,#e9c4ac,#c9997d 70%,#b58467)}
.shoulder-photo{position:absolute;right:0;top:300px;width:90px;height:120px;border-radius:50% 0 0 50%;background:linear-gradient(135deg,#d8b59c,#b98a70)}
.inside-right .copy{padding-top:16px}
.inside-right .narrow{width:180px}
.small-logo{position:absolute;bottom:18px;left:0;width:270px;display:flex;align-items:center;justify-content:center;gap:6px}
.small-logo .logo-name{font-size:9px}
.small-logo .logo-dot{width:9px;height:9px}
</style>
</head>
<body>
<div class="canvas">

  <!-- outside spread -->
  <section class="spread spread--outside">
    <div class="panel outside-left">
      <div class="about-block">
        <h3>About Kestrel Medics Bureau (KMB)</h3>
        <p>KMB is a one-of-a-kind integrated medical facility that combines the expertise of a Board Certified, Lindqvist Institute trained, Pain Management MD, and a team of physician assistants, nurse practitioners, chiropractic physicians, and physical therapists utilizing Kinetra™ therapy.</p>
        <h3>The KMB Advantage</h3>
        <ul class="advantage">
          <li>All providers under one roof</li>
          <li>Less driving - One co-pay - Save time</li>
          <li>Outside PT referrals accepted</li>
          <li>Most insurances accepted</li>
          <li>Personal Injury/Work Comp accepted</li>
          <li>Multiple Metro Locations</li>
        </ul>
        <p class="schedule">To schedule an appointment with Kestrel Medics Bureau (KMB) call today!</p>
        <div class="call">Call Today:<br>888.555.0142</div>
      </div>
      <svg class="wave" style="top:370px" width="270" height="80" viewBox="0 0 270 80" aria-hidden="true">
        <path d="M0 25 Q90 70 270 20 L270 0 L0 0 Z" fill="#0f3f7d"/>
        <path d="M0 35 Q100 75 270 30" stroke="#5b95d2" stroke-width="4" fill="none"/>
      </svg>
      <div class="contact-lower">
        <div class="serif">Blog: kmbnotes.example</div>
        <div class="serif" style="margin-top:4px">Web: kmbrelief.example</div>
        <p style="margin-top:10px"><b>Tovaria:</b> Ashdel, Brennick, Marlow, &amp; Eastvale<br><b>Corvane:</b> Lindhurst</p>
      </div>
      <svg class="wave" style="bottom:0" width="270" height="60" viewBox="0 0 270 60" aria-hidden="true">
        <path d="M0 40 Q140 0 270 30 L270 60 L0 60 Z" fill="#1b5da8"/>
      </svg>
    </div>

    <div class="panel cover">
      <div class="logo"><span class="logo-dot"></span><span class="logo-name">Kestrel Medics Bureau</span></div>
      <div class="title-band">Pain Management<br>&amp;<br>Physical Therapy Center</div>
      <div class="cover-photo" role="img" aria-label="Photo cutout of a smiling older couple riding bicycles outdoors"></div>
      <svg class="wave" style="top:410px" width="270" height="120" viewBox="0 0 270 120" aria-hidden="true">
        <path d="M0 50 Q120 0 270 40 L270 120 L0 120 Z" fill="#1b5da8"/>
        <path d="M0 70 Q130 25 270 60 L270 120 L0 120 Z" fill="#0f3f7d"/>
        <path d="M0 58 Q125 12 270 50" stroke="#cfe1f3" stroke-width="3" fill="none"/>
      </svg>
      <div style="position:absolute;top:530px;left:0;width:270px;height:85px;background:#fff"></div>
      <div class="url">www.kmbrelief.example</div>
    </div>
  </section>

  <!-- inside spread -->
  <section class="spread spread--inside">
    <div class="panel inside-left">
      <div class="band">Finding Relief</div>
      <div class="copy"><p>Whether your pain is caused by an injury, severe arthritis or a degenerative disease, we can help you find relief and regain your quality of life.</p></div>
      <div class="band">Treatments Include</div>
      <div class="copy">
        <h4>Knee Pain / Hip Pain / Arthritis</h4>
        <p>With programs nationally acclaimed by the Joint Care Guild of Tovaria, KMB uses a combination of treatments for eliminating or reducing pain quickly. Many patients with osteoarthritis may get pain relief after just one treatment. Over the last decade, our programs have helped over 5,000 patients regain their quality of life without surgery. For more information or to view success stories, visit www.zeroachelimbs.example.</p>
      </div>
      <div class="back-photo" role="img" aria-label="Cutout photo of a man's bare back with his hand on his painful shoulder"></div>
      <svg class="wave" style="bottom:0" width="270" height="90" viewBox="0 0 270 90" aria-hidden="true">
        <path d="M0 40 Q130 80 270 20 L270 90 L0 90 Z" fill="#1b5da8"/>
        <path d="M0 60 Q140 95 270 45 L270 90 L0 90 Z" fill="#0f3f7d"/>
      </svg>
    </div>

    <div class="panel inside-right">
      <div class="copy">
        <h4>Back Pain / Sciatica / Neck Pain</h4>
        <p>Our pain management treatment team, which includes a Lindqvist Institute trained physician, physical therapists, and chiropractic physicians, utilizes a multi-disciplinary approach to your pain care. If back pain is affecting your quality of life, let KMB provide you with an accurate diagnosis, rapid relief, and long lasting results.</p>
        <h4>Tennis Elbow / Rotator Cuff / Sports Injuries</h4>
        <p>KMB’s Platelet Rich Plasma (PRP) Program is the most advanced, cutting edge therapy program in the bi-state area. Using PRP, Derek Vallano, MD, can relieve your pain quickly and in a most effective way by using your blood platelets. By enhancing the tissue recovery through this unique program, athletes can get back to competition quicker, workers can return to work faster, and the average person can return to daily activities quickly. For more information about PRP, visit www.kmbrelief.example.</p>
        <h4>Peripheral Neuropathy Program (PNP)</h4>
        <p class="narrow">KMB has a solution for the irritating numbness, burning, and pain in your legs and feet. Our practice uses innovative treatment programs that will relieve your symptoms using medical treatments that are safe, effective and most importantly, require no surgery.</p>
        <h4>And more...</h4>
        <p class="narrow">SI Joint Pain, Tennis Elbow, Migraines, Headaches</p>
      </div>
      <div class="shoulder-photo" role="img" aria-label="Cutout photo of a woman holding her sore shoulder"></div>
      <svg class="wave" style="bottom:0" width="270" height="90" viewBox="0 0 270 90" aria-hidden="true">
        <path d="M0 30 Q130 70 270 25 L270 90 L0 90 Z" fill="#1b5da8"/>
        <path d="M0 48 Q130 85 270 40 L270 90 L0 90 Z" fill="#ffffff"/>
      </svg>
      <div class="small-logo"><span class="logo-dot"></span><span class="logo-name">Kestrel Medics Bureau</span></div>
    </div>
  </section>

</div>
</body>
</html>
```